Lunaryth needs a elegant mystical business card design

The theme of Lunaryth is centered on Kemetic/Ancient Egyptian Spirituality. My business sells handmade scented candles, mystic oils, body sprays, tarot readings and more. I would like my business card to reflect an elegant and mystical look. Hieroglyphs around the borders would be a cool idea. Also, the main colors I am working with is Black and Gold= colors of royalty. Black background. The business card will be double sided. The back will have the logo, and the front will have the basic information (ie name, title, business, phone, email, website, etc..)

Target Market(s)

The target market are people into metaphysics, holistic healing, ancient Egyptian culture, aromatherapy, occult science, and the esoteric.

Industry/Entity Type

Business

Contact Information for Business Card

Name: Marisol T. Pike
Title: Owner
Business: LUNARYTH
Phone: 555.210.4473
Website: www.Lunaryth.example
Facebook, Instagram, and twitter icons

Font styles to use
Serif
Decorative

Requirements
Must have
• My logo, and website.
Nice to have
• Ancient Egyptian hieroglyphs, Elegant designs around the border, or encircling the logo.

```html
<!DOCTYPE html>
<html lang="en">
<head>
<meta charset="utf-8">
<title>Lunaryth Business Card</title>
<link rel="stylesheet" href="https://fonts.googleapis.com/css2?family=Cinzel:wght@500;600&family=Marcellus&family=Open+Sans:wght@400&display=swap">
<style>
  :root {
    --backdrop: #352e29;
    --card: #121111;
    --card-edge: #1c1a19;
    --gold: #c9a053;
    --gold-soft: rgba(201, 160, 83, 0.32);
    --gold-fade: rgba(201, 160, 83, 0);
  }
  * { box-sizing: border-box; margin: 0; padding: 0; }
  html, body {
    width: 1200px;
    height: 780px;
    overflow: hidden;
    background: var(--backdrop);
  }
  .sheet {
    width: 1200px;
    height: 780px;
    display: flex;
    align-items: center;
    justify-content: center;
    gap: 40px;
  }
  .card {
    position: relative;
    width: 540px;
    height: 310px;
    background: radial-gradient(circle at 50% 40%, var(--card-edge), var(--card) 75%);
    box-shadow: 0 14px 30px rgba(0, 0, 0, 0.45);
    overflow: hidden;
    color: var(--gold);
  }
  .corner-ornament {
    position: absolute;
    width: 96px;
    height: 96px;
  }
  .corner-ornament.top-left { top: 10px; left: 10px; background: radial-gradient(circle at 20% 20%, var(--gold-soft), var(--gold-fade) 70%); }
  .corner-ornament.top-right { top: 10px; right: 10px; background: radial-gradient(circle at 80% 20%, var(--gold-soft), var(--gold-fade) 70%); }
  .corner-ornament.bottom-left { bottom: 10px; left: 10px; background: radial-gradient(circle at 20% 80%, var(--gold-soft), var(--gold-fade) 70%); }
  .corner-ornament.bottom-right { bottom: 10px; right: 10px; background: radial-gradient(circle at 80% 80%, var(--gold-soft), var(--gold-fade) 70%); }
  .edge-rules {
    position: absolute;
    inset: 0;
    width: 100%;
    height: 100%;
  }
  .brand-name {
    position: absolute;
    font-family: "Cinzel", serif;
    font-weight: 600;
    color: var(--gold);
    letter-spacing: 0.16em;
    text-align: center;
    white-space: nowrap;
  }
  .card-back .brand-name {
    left: 0;
    right: 0;
    top: 132px;
    font-size: 34px;
  }
  .card-front .brand-name {
    left: 222px;
    width: 260px;
    top: 62px;
    font-size: 26px;
  }
  .person {
    position: absolute;
    left: 222px;
    width: 260px;
    top: 118px;
    text-align: center;
  }
  .person-name {
    font-family: "Cinzel", serif;
    font-weight: 600;
    font-size: 17px;
    letter-spacing: 0.06em;
  }
  .person-title {
    font-family: "Open Sans", sans-serif;
    font-size: 11px;
    margin-top: 1px;
  }
  .contact {
    position: absolute;
    left: 150px;
    top: 170px;
    list-style: none;
    font-family: "Marcellus", serif;
    font-size: 15px;
    line-height: 21px;
  }
  .contact .phone { padding-left: 70px; }
  .contact .web { font-size: 15px; }
</style>
</head>
<body>
<main class="sheet">

  <section class="card card-back" aria-label="Card back">
    <div class="corner-ornament top-left" role="img" aria-label="Gold filigree corner ornament"></div>
    <div class="corner-ornament top-right" role="img" aria-label="Gold filigree corner ornament"></div>
    <div class="corner-ornament bottom-left" role="img" aria-label="Gold filigree corner ornament"></div>
    <div class="corner-ornament bottom-right" role="img" aria-label="Gold filigree corner ornament"></div>
    <svg class="edge-rules" viewBox="0 0 540 310" aria-hidden="true">
      <g fill="var(--gold)">
        <polygon points="100,24 190,26 100,28"/>
        <polygon points="440,282 350,284 440,286"/>
        <polygon points="24,110 26,190 28,110"/>
        <polygon points="512,200 514,120 516,200"/>
      </g>
    </svg>
    <div class="brand-name">LUNARYTH</div>
  </section>

  <section class="card card-front" aria-label="Card front">
    <div class="corner-ornament top-left" role="img" aria-label="Gold filigree corner ornament"></div>
    <div class="corner-ornament top-right" role="img" aria-label="Gold filigree corner ornament"></div>
    <div class="corner-ornament bottom-left" role="img" aria-label="Gold filigree corner ornament"></div>
    <div class="corner-ornament bottom-right" role="img" aria-label="Gold filigree corner ornament"></div>
    <svg class="edge-rules" viewBox="0 0 540 310" aria-hidden="true">
      <g fill="var(--gold)">
        <polygon points="100,24 190,26 100,28"/>
        <polygon points="440,282 350,284 440,286"/>
        <polygon points="24,110 26,190 28,110"/>
        <polygon points="512,200 514,120 516,200"/>
      </g>
    </svg>
    <div class="brand-name">LUNARYTH</div>
    <div class="person">
      <p class="person-name">EMPLOYEE NAME</p>
      <p class="person-title">Owner</p>
    </div>
    <ul class="contact">
      <li class="phone">555.210.4473</li>
      <li class="email">hello@lunaryth.example</li>
      <li class="web">www.Lunaryth.example</li>
    </ul>
  </section>

</main>
</body>
</html>
```